Packaging Design Job - Baby Diaper Rash Cream and Wipes Packaging Concepts Needed

Hello, Our baby brand “Pellora” is launching 2 new products – a Diaper Rash Cream and Diaper Wipes – and would like some creative design concepts for our product packaging.Pellora is a pharmaceutical brand that specializes in baby products. We are a mid – premium priced brand with a focus on targeting mothers between the ages of 18 – 35 years. Our products are positioned for mass market with other competitive brands such as Malvotex, Bramolux, Harvonel, and Quilbrat, to give you a better understanding of the category. What we are looking for in our packaging is an ethical, pharmaceutical look that will appeal to mothers as a product that is safe and effective for their baby. The packaging should be clean, fresh, and consumer friendly, while still maintaining that this is a clinical product. The design concepts are a box design for the Diaper Rash Cream and a plastic packaging design for the Diaper Wipes. Attached you will find the Pellora logo and examples of Diaper Rash Cream box packaging and Diaper Wipes plastic packaging from competitors (to give you an idea of what shape of packaging we like). Please feel free to contact me should you have any questions.Thank you for your time and effort,Roxa

Target Market(s)

We are a mid – premium priced brand with a focus on targeting mothers between the ages of 18 – 35 years.

Industry/Entity Type

Baby Care

Requirements
Must have
• Packaging design concepts for a box design for the Diaper Rash Cream and a plastic packaging design for the Diaper Wipes.
Nice to have
• Diaper Rash Cream box: 8 cm width, 8 cm length, 8 cm depth
• Diaper Wipes package: 23 cm width, 10.5 cm length, 4.5 cm depth

```html
<!DOCTYPE html>
<html lang="en">
<head>
<meta charset="utf-8">
<title>Pellora Natural Clean Baby Wipes – Pack Front</title>
<link rel="stylesheet" href="https://fonts.googleapis.com/css2?family=Montserrat:wght@300;400;800&display=swap">
<style>
  :root {
    --page: #ffffff;
    --panel-top: #eeedee;
    --panel-bottom: #e9e7e8;
    --rose: #dfa294;
    --rose-deep: #dca69a;
    --taupe: #cec7c2;
    --soft-copy: #c89c92;
    --band-peach: #e4b9ad;
    --band-pink: #efc2cf;
    --skin: #f0cdbf;
    --blanket: #fbfafa;
    --aloe: #6f9a55;
  }
  * { margin: 0; padding: 0; box-sizing: border-box; }
  html, body {
    width: 1200px; height: 753px; overflow: hidden;
    background: var(--page);
    font-family: "Montserrat", sans-serif;
  }
  .canvas { position: relative; width: 1200px; height: 753px; }
  .pack-front {
    position: absolute; left: 137px; top: 130px;
    width: 927px; height: 423px; overflow: hidden;
    background: linear-gradient(180deg, var(--panel-top), var(--panel-bottom));
  }
  .hero-photo {
    position: absolute; left: 0; top: 0; width: 440px; height: 423px;
    background:
      radial-gradient(ellipse 150px 190px at 250px 230px, var(--skin) 0%, rgba(240,205,191,0.7) 55%, rgba(240,205,191,0) 100%),
      radial-gradient(ellipse 240px 160px at 200px 330px, var(--blanket) 0%, rgba(251,250,250,0) 100%);
  }
  .wave-band { position: absolute; left: 0; top: 0; width: 927px; height: 423px; }
  .brand-name {
    position: absolute; left: 712px; top: 61px;
    display: flex; align-items: center; gap: 8px;
    font-weight: 800; font-size: 28px; line-height: 1; letter-spacing: 1px;
    color: var(--rose-deep); text-transform: uppercase; white-space: nowrap;
  }
  .brand-dot {
    width: 11px; height: 11px; border-radius: 50%;
    background: var(--rose-deep); flex: none;
  }
  .product-line {
    position: absolute; left: 354px; top: 96px;
    font-weight: 300; font-size: 36px; line-height: 1; color: var(--rose);
    letter-spacing: -0.5px; white-space: nowrap;
  }
  .product-name {
    position: absolute; left: 352px; top: 134px;
    font-weight: 800; font-size: 90px; line-height: 1;
    letter-spacing: -4px; white-space: nowrap;
  }
  .product-name .baby { color: var(--taupe); }
  .product-name .wipes { color: var(--rose); }
  .claim {
    position: absolute; left: 451px; top: 270px;
    font-weight: 300; font-size: 28px; line-height: 1; color: var(--rose);
    letter-spacing: -0.4px; white-space: nowrap;
  }
  .soothing {
    position: absolute; left: 525px; top: 354px;
    display: flex; align-items: center; gap: 4px;
  }
  .aloe-art {
    width: 52px; height: 46px;
    background: radial-gradient(ellipse 24px 20px at 50% 65%, var(--aloe), rgba(111,154,85,0) 100%);
  }
  .soothing-text {
    font-weight: 300; font-size: 16.5px; color: var(--soft-copy);
    letter-spacing: -0.3px; white-space: nowrap;
  }
</style>
</head>
<body>
<div class="canvas">
  <section class="pack-front">
    <div class="hero-photo" role="img" aria-label="Photo of a sleeping newborn lying on a soft white blanket"></div>

    <svg class="wave-band" viewBox="0 0 927 423" aria-hidden="true">
      <path d="M0,330 C60,380 150,416 300,423 L0,423 Z" fill="var(--band-peach)" opacity="0.85"/>
      <path d="M260,423 C450,360 600,330 720,332 C820,334 880,345 927,352 L927,392 C870,370 800,358 720,358 C600,360 450,395 330,423 Z" fill="var(--band-pink)" opacity="0.9"/>
    </svg>

    <div class="brand-name"><span class="brand-dot"></span>Pellora</div>

    <p class="product-line">Natural Clean</p>
    <h1 class="product-name"><span class="baby">Baby</span><span class="wipes">Wipes</span></h1>
    <p class="claim">Chemical &amp; Allergy Free</p>

    <div class="soothing">
      <div class="aloe-art" role="img" aria-label="Illustration of an aloe vera plant"></div>
      <span class="soothing-text">Naturally Soothing</span>
    </div>
  </section>
</div>
</body>
</html>
```